Website Home Page for Women's Health Medical Office

Redesign existing homepage for website using existing logo. Current website location is www.lumawomenscare.com. Please give it a modern, streamlined, playful feel.

Please give it a feminine feel and make it bright and cheerful using logo colors.

Target Market(s)

Women between the ages of 25-45

Industry/Entity Type

Medical Office

Coding

Coded - Design and coding required

Number of Pages Required

1 page

Font styles to use
Sans Serif
Other font styles liked:
• SEGOI UI script for text and GIL SANS for bold (or their equivilent)

Colors
E54698
E96AAD
F1A4CE
F9D9EA
FCEFF6

Requirements
Must have
• Existing logo. Logo Colors. Feminine, cheerful, simple design. all relevant contact information
Nice to have
• clean lines and streamlined look
Should not have
• Cluttered

```html
<!DOCTYPE html>
<html lang="en">
<head>
<meta charset="utf-8">
<title>Luma OB/GYN – Personalized Medical Care for Women</title>
<link rel="stylesheet" href="https://fonts.googleapis.com/css2?family=Cabin:ital,wght@0,400;0,600;0,700;1,400;1,600&family=Lato:ital,wght@0,300;1,300&family=Open+Sans:wght@400;600&display=swap">
<style>
:root{
  --pink-deep:#E54698;
  --pink:#E96AAD;
  --pink-mid:#F1A4CE;
  --pink-soft:#F9D9EA;
  --pink-pale:#FCEFF6;
  --hero-a:#f27fb6;
  --hero-b:#f7a3ca;
  --ink:#2f2f2f;
  --body:#4a4a4a;
  --footer:#262626;
  --white:#ffffff;
}
*{box-sizing:border-box;margin:0;padding:0}
html,body{width:1200px;height:4033px;overflow:hidden}
body{position:relative;font-family:"Open Sans",sans-serif;color:var(--body);background:var(--white)}
.abs{position:absolute}
.heading{font-family:"Cabin",sans-serif;font-weight:700;color:var(--ink)}
.script{font-family:"Lato",sans-serif;font-style:italic;font-weight:300}
.btn{position:absolute;display:flex;align-items:center;justify-content:center;gap:8px;border-radius:30px;font-family:"Open Sans",sans-serif;font-size:16px;color:var(--white);background:linear-gradient(90deg,var(--pink),var(--pink-mid))}
.btn svg{width:12px;height:12px}
.photo{position:absolute;border-radius:18px}
.deco{position:absolute;border-radius:50%}

/* hero */
.hero{position:absolute;left:0;top:0;width:1200px;height:585px;background:linear-gradient(110deg,var(--hero-a),var(--hero-b));overflow:hidden}
.hero-photo{position:absolute;left:735px;top:70px;width:465px;height:515px;background:linear-gradient(160deg,#f7c4dc,#e9b79f 55%,#f3e7e0);border-radius:200px 0 0 0}
.ribbon{position:absolute;left:350px;top:-40px;width:420px;height:180px;border-radius:50%;background:radial-gradient(ellipse,rgba(255,255,255,.45),rgba(255,255,255,0) 70%)}
.brand{position:absolute;left:100px;top:48px;display:flex;align-items:center;gap:10px;font-family:"Cabin",sans-serif;font-weight:700;font-size:24px;color:var(--white)}
.brand .dot{width:16px;height:16px;border-radius:50%;background:var(--white)}
.nav{position:absolute;top:27px;display:flex;font-size:15px;color:var(--white)}
.nav a{position:absolute;color:var(--white);text-decoration:none;white-space:nowrap}
.phone-pill{position:absolute;left:939px;top:16px;width:261px;height:46px;border-radius:23px 0 0 23px;background:var(--pink-deep);display:flex;align-items:center;gap:12px;padding-left:8px;color:var(--white);font-weight:600;font-size:16px}
.phone-pill .ico{width:32px;height:32px;border-radius:50%;background:var(--pink-mid);display:flex;align-items:center;justify-content:center}
.hero-title{position:absolute;left:97px;top:185px;font-family:"Cabin",sans-serif;font-weight:700;font-size:35px;line-height:46px;color:var(--white)}
.hero-btn{position:absolute;left:98px;top:350px;width:248px;height:47px;border:2px solid var(--white);border-radius:24px;display:flex;align-items:center;justify-content:center;gap:8px;color:var(--white);font-size:16px}
.dots{position:absolute;left:100px;top:522px;display:flex;gap:14px}
.dots span{width:12px;height:12px;border:1.5px solid var(--white)}
.dots span.on{background:var(--white)}

/* welcome */
.welcome-photo{left:94px;top:673px;width:422px;height:454px;background:radial-gradient(circle at 55% 45%,#efc3a7 0 22%,#3b3f63 45%,#f7b7d6 46%,#fbe0ee 75%,var(--white) 76%);border-radius:0}
.welcome-kicker{left:527px;top:686px;font-family:"Cabin",sans-serif;font-size:33px;color:var(--ink)}
.welcome-title{left:527px;top:724px;font-size:38px}
.welcome-sub{left:527px;top:772px;font-family:"Cabin",sans-serif;font-style:italic;font-weight:600;font-size:26px;color:var(--ink)}
.copy{position:absolute;font-size:15px;line-height:26px;color:var(--body)}
.signature{left:516px;top:1127px;width:157px;height:78px;background:linear-gradient(90deg,var(--pink-pale),var(--white));border-radius:8px}

/* services */
.services{position:absolute;left:0;top:1255px;width:1200px;height:579px;background:var(--pink-soft)}
.sec-title{position:absolute;left:0;width:1200px;text-align:center}
.card{position:absolute;top:1408px;width:235px}
.card .frame{position:absolute;left:8px;top:-8px;width:235px;height:158px;border-top:3px solid var(--pink);border-right:3px solid var(--pink);border-radius:0 14px 0 0}
.card .img{position:relative;width:235px;height:158px;border-radius:12px}
.card h3{font-family:"Cabin",sans-serif;font-weight:700;font-size:21px;color:var(--ink);margin-top:10px}
.card p{font-size:16px;line-height:23px;margin-top:4px;height:90px}
.card .btn{position:absolute;top:301px;width:153px;height:47px}

/* about */
.about-frame{left:672px;top:1908px;width:428px;height:445px;border-top:4px solid var(--pink);border-right:4px solid var(--pink);border-radius:0 24px 0 0}

/* patients */
.patients{position:absolute;left:0;top:2418px;width:1200px;height:579px;background:var(--pink-soft)}
.pat-frame{left:130px;top:2470px;width:430px;height:470px;border-top:4px solid var(--pink);border-right:4px solid var(--pink);border-radius:0 24px 0 0}

/* contact */
.contact-card{position:absolute;left:183px;top:3075px;width:833px;height:481px;border-radius:0 60px 60px 60px;overflow:hidden;display:flex}
.map{width:418px;height:481px;background:linear-gradient(160deg,#ececec,#f2e4e4 60%,#efd3d6)}
.contact-panel{position:relative;width:415px;height:481px;background:linear-gradient(180deg,var(--pink-mid),#f592bf)}
.contact-panel h2{position:absolute;left:47px;top:72px;font-family:"Cabin",sans-serif;font-weight:700;font-size:46px;color:var(--white)}
.field{position:absolute;left:47px;width:354px;background:var(--white);border-radius:4px;font-size:14px;color:#555;padding:10px 10px}
.submit{position:absolute;left:52px;top:362px;width:148px;height:47px;border:2px solid var(--white);border-radius:24px;display:flex;align-items:center;justify-content:center;gap:6px;color:var(--white);font-size:16px}

/* footer */
.footer{position:absolute;left:0;top:3625px;width:1200px;height:408px;background:var(--footer);color:#d6d6d6}
.footer .fbrand{position:absolute;left:100px;top:110px;display:flex;align-items:center;gap:10px;font-family:"Cabin",sans-serif;font-weight:700;font-size:24px;color:var(--pink)}
.footer .fbrand .dot{width:14px;height:14px;border-radius:50%;background:var(--pink)}
.footer h4{position:absolute;top:78px;font-family:"Cabin",sans-serif;font-weight:700;font-size:18px;color:var(--white)}
.links{position:absolute;left:357px;top:122px;list-style:none;font-size:14px;line-height:34.4px}
.links li::before{content:"›";color:var(--pink);margin-right:8px}
.finfo{position:absolute;left:574px;font-size:14px;line-height:26px;display:flex;gap:10px}
.finfo svg{width:14px;height:14px;margin-top:6px;flex:none}
.news-input{position:absolute;left:834px;top:3757px;width:269px;height:41px;border-radius:20px;background:var(--white);font-size:14px;color:#555;padding:11px 22px}
.news-btn{position:absolute;left:834px;top:3809px;width:269px;height:41px;border-radius:20px;background:linear-gradient(90deg,var(--pink),var(--pink-mid));color:var(--white);font-size:15px;display:flex;align-items:center;justify-content:center}
.divider{position:absolute;left:97px;top:3975px;width:1006px;height:1px;background:#555}
.copyright{position:absolute;left:0;top:3993px;width:1200px;text-align:center;font-size:14px;color:#bbb}
.copyright span{color:var(--pink)}
</style>
</head>
<body>

<!-- Hero -->
<header class="hero">
  <div class="ribbon" role="img" aria-label="Soft flowing silk ribbon"></div>
  <div class="hero-photo" role="img" aria-label="Photo of a smiling pregnant woman holding her belly"></div>
  <div class="brand"><span class="dot"></span>Luma OB/GYN</div>
  <nav class="nav">
    <a style="left:429px">Home</a>
    <a style="left:513px">About us</a>
    <a style="left:616px">Services</a>
    <a style="left:717px">Resources</a>
    <a style="left:831px">Contact us</a>
  </nav>
  <div class="phone-pill">
    <span class="ico"><svg width="16" height="16" viewBox="0 0 24 24" fill="#fff"><path d="M6.6 10.8a15 15 0 006.6 6.6l2.2-2.2a1 1 0 011-.25 11.4 11.4 0 003.6.57 1 1 0 011 1V20a1 1 0 01-1 1A17 17 0 013 4a1 1 0 011-1h3.5a1 1 0 011 1c0 1.25.2 2.45.57 3.57a1 1 0 01-.25 1z"/></svg></span>
    (555) 014-7066
  </div>
  <h1 class="hero-title">Our Medical providers<br>will take time to give you<br>the Personalized Health Care</h1>
  <div class="hero-btn">Schedule Appointment <svg width="12" height="12" viewBox="0 0 12 12" fill="none" stroke="#fff" stroke-width="1.6"><path d="M1 6h9M6.5 2.5L10 6l-3.5 3.5"/></svg></div>
  <div class="dots"><span class="on"></span><span></span><span></span></div>
</header>

<!-- Welcome -->
<section class="welcome">
  <div class="photo abs welcome-photo" role="img" aria-label="Portrait of a smiling doctor in navy scrubs over a pink dotted circle"></div>
  <p class="abs welcome-kicker">Welcome to</p>
  <h2 class="abs heading welcome-title">Luma OB/GYN, Larkfield, CA</h2>
  <p class="abs welcome-sub">Serving Valley Springs Medical center</p>
  <p class="copy" style="left:527px;top:818px;width:580px">At Luma OB/GYN in Larkfield, California, we believe better health starts when the patient is educated. For this reason, we take time to listen to our patients concerns, explain each option available, and to answer any questions our patients may have so that they can make informed decisions. At Luma OB/GYN, our providers tailor every procedure performed and treatment option recommended to meet the specific needs of our patients. We remain up-to-date on the latest technology and practice guidelines for women's health.</p>
  <p class="copy" style="left:527px;top:1005px;width:580px">Our medical providers will take time to give you the personalized health care you deserve. This includes taking time to listen to you and screening you for problems to help ensure that any health issues are diagnosed and treated as early as possible.</p>
  <div class="abs signature" role="img" aria-label="Handwritten signature"></div>
</section>

<!-- Services -->
<section class="services">
  <div class="deco" style="left:1090px;top:30px;width:110px;height:110px;background:var(--pink-mid);opacity:.5" role="img" aria-label="Female symbol decoration"></div>
  <h2 class="sec-title heading" style="top:50px;font-size:37px;letter-spacing:1px">HOW CAN WE HELP YOU?</h2>
  <p class="sec-title" style="top:92px;font-family:'Cabin',sans-serif;font-size:26px;color:var(--ink)">Health Services Offered</p>
</section>
<div class="card" style="left:98px">
  <div class="frame"></div>
  <div class="img" style="background:linear-gradient(135deg,#f3ece6,#e8c8b4)" role="img" aria-label="Hands forming a heart on a pregnant belly"></div>
  <h3>Pregnancy care</h3>
  <p>Receiving regular care in pregnancy is important for the health of both you and your baby.</p>
  <div class="btn">Learn More <svg viewBox="0 0 12 12" fill="none" stroke="#fff" stroke-width="1.6"><path d="M1 6h9M6.5 2.5L10 6l-3.5 3.5"/></svg></div>
</div>
<div class="card" style="left:354px">
  <div class="frame"></div>
  <div class="img" style="background:linear-gradient(135deg,#efe7e1,#b48a70)" role="img" aria-label="Woman holding a birth control pill pack"></div>
  <h3>Birth control</h3>
  <p>Our gynecologists are knowledgeable on all forms of birth control including</p>
  <div class="btn">Learn More <svg viewBox="0 0 12 12" fill="none" stroke="#fff" stroke-width="1.6"><path d="M1 6h9M6.5 2.5L10 6l-3.5 3.5"/></svg></div>
</div>
<div class="card" style="left:609px">
  <div class="frame"></div>
  <div class="img" style="background:linear-gradient(135deg,#5c6b72,#9aa7ad)" role="img" aria-label="Woman stretching in bed after waking up"></div>
  <h3>Well woman exams</h3>
  <p>Our providers will help you to stay healthy by performing a physical exam on you annually</p>
  <div class="btn">Learn More <svg viewBox="0 0 12 12" fill="none" stroke="#fff" stroke-width="1.6"><path d="M1 6h9M6.5 2.5L10 6l-3.5 3.5"/></svg></div>
</div>
<div class="card" style="left:864px">
  <div class="frame"></div>
  <div class="img" style="background:linear-gradient(160deg,#d9e6ee,#f3f1ec)" role="img" aria-label="Woman with open arms outdoors"></div>
  <h3>Women's health</h3>
  <p>Whether you are dealing with painful or irregular periods, fibroids, or other</p>
  <div class="btn">Learn More <svg viewBox="0 0 12 12" fill="none" stroke="#fff" stroke-width="1.6"><path d="M1 6h9M6.5 2.5L10 6l-3.5 3.5"/></svg></div>
</div>

<!-- About -->
<section class="about">
  <div class="deco" style="left:436px;top:1865px;width:112px;height:112px;background:var(--pink-soft)" role="img" aria-label="Female symbol decoration"></div>
  <h2 class="abs heading" style="left:102px;top:1972px;font-size:38px">About Us</h2>
  <p class="copy" style="left:95px;top:2024px;width:480px">Luma OB/GYN in Larkfield, California, was formed in October of 2005 by Dr. Owen Marsh and Dr. Clara Wendt. to help service the greats need for women's health services in Southwest Riverside County. In October of 2012, Dr. Marsh retired, and Dr. Nora Avery joined the practice. In December of 2015, Dr. Avery left the practice, leaving Dr. Wendt to carry on as a solo practitioner. In November of 2022, Dr. Leah Morrow joined the Luma OB/GYN family.</p>
  <div class="btn" style="left:98px;top:2261px;width:165px;height:47px">Read More <svg viewBox="0 0 12 12" fill="none" stroke="#fff" stroke-width="1.6"><path d="M1 6h9M6.5 2.5L10 6l-3.5 3.5"/></svg></div>
  <div class="abs about-frame"></div>
  <div class="photo" style="left:612px;top:1918px;width:476px;height:468px;background:linear-gradient(135deg,#c9cdd0,#8f969c 45%,#c79a7e)" role="img" aria-label="Doctor examining a pregnant patient on a couch"></div>
</section>

<!-- New patients -->
<section class="patients">
  <div class="deco" style="left:1016px;top:130px;width:110px;height:110px;background:var(--pink-mid);opacity:.45" role="img" aria-label="Female symbol decoration"></div>
</section>
<div class="abs pat-frame"></div>
<div class="photo" style="left:98px;top:2480px;width:454px;height:470px;background:linear-gradient(135deg,#f4f4f2,#d8d6d4 55%,#7e9a6c)" role="img" aria-label="Pregnant woman in a cardigan holding her belly near a plant"></div>
<p class="abs script" style="left:584px;top:2474px;font-size:32px;color:var(--ink)">Better Health Starts Here!</p>
<h2 class="abs heading" style="left:584px;top:2512px;font-size:45px;line-height:47px">Now accepting<br>New patients</h2>
<p class="abs" style="left:584px;top:2616px;font-style:italic;font-size:19px;line-height:29px;color:var(--ink)">Click Here for an Appointment<br>or Call Us At (555) 014-7066</p>
<h3 class="abs heading" style="left:584px;top:2677px;font-size:28px">Your ob/gyn specialists</h3>
<p class="copy" style="left:586px;top:2722px;width:520px">Luma OB/GYN offers you the best care possible in a personalized setting. We are currently accepting patients. Call our office now to make an appointment.</p>
<p class="copy" style="left:586px;top:2806px;width:520px">Luma OB/GYN (located near Valley Springs Hospital in Larkfield, CA) is a medical office that specializes in Christ-centered healthcare for women of all ages.</p>
<div class="btn" style="left:588px;top:2900px;width:165px;height:46px">Read More <svg viewBox="0 0 12 12" fill="none" stroke="#fff" stroke-width="1.6"><path d="M1 6h9M6.5 2.5L10 6l-3.5 3.5"/></svg></div>

<!-- Contact -->
<section class="contact">
  <div class="deco" style="left:1065px;top:3045px;width:38px;height:38px;background:var(--pink)" role="img" aria-label="Female symbol decoration"></div>
  <div class="deco" style="left:70px;top:3475px;width:66px;height:66px;background:var(--pink-soft)" role="img" aria-label="Female symbol decoration"></div>
  <div class="contact-card">
    <div class="map" role="img" aria-label="Street map showing the office near Valley Springs Medical Center"></div>
    <div class="contact-panel">
      <h2>Contact Us</h2>
      <div class="field" style="top:135px;height:45px">Name</div>
      <div class="field" style="top:189px;height:44px">Email</div>
      <div class="field" style="top:244px;height:97px">Your Message</div>
      <div class="submit">Submit <svg width="12" height="12" viewBox="0 0 12 12" fill="none" stroke="#fff" stroke-width="1.6"><path d="M1 6h9M6.5 2.5L10 6l-3.5 3.5"/></svg></div>
    </div>
  </div>
</section>

<!-- Footer -->
<footer class="footer">
  <div class="fbrand"><span class="dot"></span>Luma OB/GYN</div>
  <h4 style="left:357px">Quick Links</h4>
  <ul class="links">
    <li>Home</li><li>About us</li><li>News</li><li>Patient resources</li><li>Privacy policy</li><li>Contact us</li>
  </ul>
  <h4 style="left:574px">Contact Us</h4>
  <div class="finfo" style="top:122px"><svg viewBox="0 0 24 24" fill="#E96AAD"><path d="M12 2a7 7 0 00-7 7c0 5 7 13 7 13s7-8 7-13a7 7 0 00-7-7zm0 9.5A2.5 2.5 0 1112 6a2.5 2.5 0 010 5.5z"/></svg><span>1840 Orchard Avenue,<br>Suite 210, Larkfield, CA<br>90210</span></div>
  <div class="finfo" style="top:203px"><svg viewBox="0 0 24 24" fill="#E96AAD"><path d="M6.6 10.8a15 15 0 006.6 6.6l2.2-2.2a1 1 0 011-.25 11.4 11.4 0 003.6.57 1 1 0 011 1V20a1 1 0 01-1 1A17 17 0 013 4a1 1 0 011-1h3.5a1 1 0 011 1c0 1.25.2 2.45.57 3.57a1 1 0 01-.25 1z"/></svg><span>(555) 014-7066</span></div>
  <div class="finfo" style="top:237px"><svg viewBox="0 0 24 24" fill="#E96AAD"><path d="M6 3h10v5H6zM3 9h18v11H3zm4 3v2h3v-2zm0 4v2h3v-2zm6-4v2h5v-2z"/></svg><span>(555) 014-7793</span></div>
  <div class="finfo" style="top:271px"><svg viewBox="0 0 24 24" fill="#E96AAD"><path d="M3 5h18v14H3zm2 2v.5l7 5 7-5V7l-7 5z"/></svg><span>admin@lumawomenscare.com</span></div>
  <h4 style="left:834px">Newsletter</h4>
</footer>
<div class="news-input">Enter email address</div>
<div class="news-btn">Subscribe→</div>
<div class="divider"></div>
<p class="copyright">© 2022 <span>Luma OB/GYN</span>. All right reserved</p>

</body>
</html>
```